website for MapleHarbor Partners - a HR Consultancy Company

Creation of a website template. I would like to make it with with Wix, but am open to other online website programms.

Website is for consulting company in human resources offering the following services:
- Human resources and talent management for small companies
- Human resources consulting for start-ups
- Diversity and Inclusion management/training
- Board of Directors - talent identification and need evalutation
- coaching and counseling

Pages needed:
- Home page
- HR and talent management
- HR consulting for start-ups
- Diversity & Inclusion management/training
- coaching and counseling
- contact

1. My logo below
2. an example website that I like (not in terms of colours): https://www.quillbrookadvisory.ch/
http://www.veltrimaxon.ch/

Target Market(s)

small and mid-sized companies, start-ups

Industry/Entity Type

Consulting

Number of Pages Required

5+ page

Font styles to use
Serif
Sans Serif

Colors
3277b5
35a7d7

Requirements
Must have
• - easy on the eye yet professional looking
• - my text is short
• - website should be clear and easy to understand
Nice to have
• - I will include photographs of the coaches
Should not have
• too many colours
• complicated

```html
<!DOCTYPE html>
<html lang="en">
<head>
<meta charset="utf-8">
<title>MapleHarbor Partners — HR Consultancy</title>
<link rel="stylesheet" href="https://fonts.googleapis.com/css2?family=Roboto+Condensed:wght@400;700&family=Open+Sans:wght@400;600&display=swap">
<style>
:root{
  --blue:#2f6fba;
  --blue-dark:#1d57a3;
  --blue-deep:#14468c;
  --sky:#35a7d7;
  --ink:#222;
  --text:#555;
  --muted:#888;
  --light:#f3f3f3;
  --footer-top:#3a3a3a;
  --footer-bottom:#202020;
  --white:#fff;
}
*{box-sizing:border-box;margin:0;padding:0}
html,body{width:1200px;height:3136px;overflow:hidden}
body{font-family:"Open Sans",Arial,sans-serif;color:var(--text);background:var(--white);position:relative}
.heading{font-family:"Roboto Condensed","Arial Narrow",sans-serif;font-weight:400;color:var(--ink)}
.abs{position:absolute}

/* header */
.site-header{position:absolute;left:0;top:0;width:1200px;height:125px;background:var(--white);box-shadow:0 2px 6px rgba(0,0,0,.06);z-index:3}
.brand{position:absolute;left:90px;top:30px;display:flex;align-items:center;gap:12px}
.brand-mark{width:34px;height:34px;border-radius:50%;background:var(--blue)}
.brand-name{font-family:"Roboto Condensed",sans-serif;font-weight:700;font-size:21px;line-height:24px;color:var(--blue-dark);letter-spacing:.5px}
.main-nav{position:absolute;left:392px;top:50px;display:flex;align-items:center;font-size:17px;color:#333}
.main-nav a{color:inherit;text-decoration:none;margin-right:44px}
.main-nav a.active{background:var(--blue);color:var(--white);border-radius:16px;padding:5px 24px;margin-right:32px}
.search-icon{position:absolute;left:1083px;top:52px}

/* hero */
.hero{position:absolute;left:0;top:125px;width:1200px;height:570px;overflow:hidden}
.hero-photo{position:absolute;inset:0;background:linear-gradient(110deg,#f4f8fc 0%,#e2ecf6 40%,#c9d9ea 70%,#b3c7dc 100%)}
.hero-title{position:absolute;left:88px;top:210px;font-family:"Roboto Condensed",sans-serif;font-size:58px;color:var(--blue);letter-spacing:.5px}
.hero-sub{position:absolute;left:88px;top:276px;font-size:27px;color:#222}
.hero-dots{position:absolute;left:88px;top:335px;display:flex;gap:4px}
.hero-dots span{width:20px;height:20px;border-radius:50%;background:#666}
.hero-curve{position:absolute;left:0;top:0}

/* services */
.services-title{position:absolute;left:0;top:765px;width:1200px;text-align:center;font-size:38px}
.intro{position:absolute;left:150px;top:828px;width:900px;text-align:center;font-size:14.5px;line-height:24px;color:var(--muted)}
.service{position:absolute;top:920px;width:300px;text-align:center}
.service-icon{width:102px;height:102px;margin:0 auto;border-radius:50%;border:2px solid var(--blue);padding:5px}
.service-icon div{width:100%;height:100%;border-radius:50%;background:var(--blue);display:flex;align-items:center;justify-content:center}
.service h3{font-weight:400;font-size:17px;line-height:23px;color:#333;margin-top:30px}
.service p{font-size:13.5px;line-height:20px;color:var(--muted);margin-top:9px}
.slider-arrow{position:absolute;top:1010px;width:38px;height:38px;border-radius:50%;background:var(--white);box-shadow:0 1px 5px rgba(0,0,0,.15);display:flex;align-items:center;justify-content:center}

/* welcome */
.welcome{position:absolute;left:0;top:1250px;width:1200px;height:455px;overflow:hidden}
.welcome-photo{position:absolute;left:600px;top:0;width:600px;height:455px;background:linear-gradient(120deg,#d9dfe4,#b9c3cc 45%,#8e9eaa)}
.welcome-panel{position:absolute;left:0;top:0}
.welcome h2{position:absolute;left:90px;top:68px;font-family:"Roboto Condensed",sans-serif;font-weight:400;font-size:37px;color:var(--white)}
.welcome p{position:absolute;left:90px;top:128px;width:525px;font-size:14px;line-height:25.5px;color:var(--white);text-align:justify}
.btn-outline{position:absolute;left:84px;top:330px;width:124px;height:38px;border:1.5px solid var(--white);border-radius:20px;color:var(--white);font-size:13px;display:flex;align-items:center;justify-content:center}

/* what we do */
.wwd-frame{position:absolute;left:92px;top:1806px;width:338px;height:378px;background:var(--blue)}
.wwd-photo{position:absolute;left:110px;top:1826px;width:336px;height:358px;background:linear-gradient(135deg,#dfe6ec,#a9b8c5 55%,#6f8396);box-shadow:6px 10px 22px rgba(0,0,0,.25)}
.wwd-title{position:absolute;left:512px;top:1830px;font-size:34px}
.wwd-text{position:absolute;left:512px;top:1888px;width:595px;font-size:13.5px;line-height:23px;color:var(--text);text-align:justify}
.ticks{position:absolute;left:512px;top:1975px;list-style:none;font-size:14px;color:#333}
.ticks li{display:flex;align-items:center;gap:12px;height:35px}
.btn-solid{position:absolute;left:512px;top:2130px;width:122px;height:38px;border-radius:20px;background:var(--blue);color:var(--white);font-size:13px;display:flex;align-items:center;justify-content:center;box-shadow:0 3px 6px rgba(0,0,0,.2)}

/* blog */
.blog{position:absolute;left:0;top:2276px;width:1200px;height:534px;background:var(--light)}
.blog-title{position:absolute;left:0;top:54px;width:1200px;text-align:center;font-size:37px}
.post{position:absolute;top:146px;width:312px}
.post-photo{height:174px}
.post-meta{display:flex;margin-top:12px;height:22px;font-size:12px}
.post-date{background:var(--blue);color:var(--white);width:70px;display:flex;align-items:center;justify-content:center}
.post-comments{background:#2a2a2a;width:38px;display:flex;align-items:center;justify-content:center}
.post h4{font-weight:400;font-size:15.5px;color:#222;margin-top:16px}
.post p{font-size:13px;line-height:20px;color:var(--muted);margin-top:5px}
.post .more{font-size:13px;color:var(--blue);margin-top:8px}

/* footer */
.site-footer{position:absolute;left:0;top:2810px;width:1200px;height:326px;background:linear-gradient(180deg,var(--footer-top),var(--footer-bottom));color:#ddd}
.footer-brand{position:absolute;left:96px;top:100px;display:flex;align-items:center;gap:10px}
.footer-brand .brand-mark{background:var(--white)}
.footer-brand .brand-name{color:var(--white)}
.foot-col{position:absolute;top:80px}
.foot-col h5{font-weight:400;font-size:15px;color:var(--white);margin-bottom:22px}
.foot-col p{font-size:12.5px;line-height:22px}
.subscribe{display:flex;margin-top:14px}
.subscribe span:first-child{width:148px;height:30px;background:var(--white);color:#888;font-size:11px;padding:8px}
.subscribe span:last-child{width:56px;height:30px;background:var(--blue);color:var(--white);font-size:12px;display:flex;align-items:center;justify-content:center}
.social{display:flex;gap:12px;margin-top:4px}
.social span{width:24px;height:24px;background:#eee;border-radius:3px}
.foot-rule{position:absolute;left:92px;top:258px;width:1016px;height:1px;background:#4a4a4a}
.copyright{position:absolute;left:0;top:280px;width:1200px;text-align:center;font-size:12px;color:#ddd}
</style>
</head>
<body>

<header class="site-header">
  <div class="brand"><span class="brand-mark"></span><span class="brand-name">MAPLEHARBOR<br>PARTNERS</span></div>
  <nav class="main-nav">
    <a class="active">Home</a><a>About us</a><a>Services</a><a>Project</a><a>Blog</a><a>Contact us</a>
  </nav>
  <svg class="search-icon" width="22" height="22" viewBox="0 0 22 22"><circle cx="9" cy="9" r="6.5" fill="none" stroke="#111" stroke-width="2.6"/><line x1="14" y1="14" x2="20" y2="20" stroke="#111" stroke-width="3"/></svg>
</header>

<section class="hero">
  <div class="hero-photo" role="img" aria-label="Smiling business team at a laptop giving thumbs up in a bright office"></div>
  <svg class="hero-curve" width="1200" height="570" viewBox="0 0 1200 570">
    <path d="M0 480 Q600 610 1200 480 L1200 570 L0 570Z" fill="#fff"/>
    <path d="M0 480 Q600 610 1200 480" fill="none" stroke="#2f6fba" stroke-width="6"/>
  </svg>
  <div class="hero-title">MAPLEHARBOR</div>
  <div class="hero-sub">Porro quisquam dolorem</div>
  <div class="hero-dots"><span></span><span></span></div>
</section>

<h2 class="heading services-title">Our Services</h2>
<p class="intro">It is a long established fact that a reader will be distracted by the readable content of a page when looking at its layout. The point of using Lorem Ipsum is that it has a more-or-less normal distribution of letters, as opposed to using 'Content here,</p>

<div class="slider-arrow" style="left:64px"><svg width="10" height="16"><path d="M8 2 L2 8 L8 14" fill="none" stroke="#555" stroke-width="1.6"/></svg></div>
<div class="slider-arrow" style="left:1098px"><svg width="10" height="16"><path d="M2 2 L8 8 L2 14" fill="none" stroke="#555" stroke-width="1.6"/></svg></div>

<div class="service" style="left:128px">
  <div class="service-icon"><div><svg width="34" height="34" viewBox="0 0 34 34"><path d="M30 4 C20 4 13 10 10 18 L16 24 C24 21 30 14 30 4Z" fill="#fff"/><path d="M10 18 L4 20 L9 14Z M16 24 L14 30 L20 25Z M9 22 L5 29 L12 25Z" fill="#fff"/></svg></div></div>
  <h3>Human resources and talent<br>management for small companies</h3>
  <p>It has survived not only five centuries,<br>but also the leap into electronic</p>
</div>
<div class="service" style="left:447px">
  <div class="service-icon"><div><svg width="40" height="34" viewBox="0 0 40 34"><circle cx="20" cy="9" r="5" fill="#fff"/><circle cx="9" cy="12" r="4" fill="#fff"/><circle cx="31" cy="12" r="4" fill="#fff"/><path d="M11 28 Q11 16 20 16 Q29 16 29 28Z M1 28 Q1 18 9 18 Q12 18 13 19 Q9 23 9 28Z M39 28 Q39 18 31 18 Q28 18 27 19 Q31 23 31 28Z" fill="#fff"/></svg></div></div>
  <h3>Human resources<br>consulting for start-ups</h3>
  <p>It has survived not only five centuries,<br>but also the leap into electronic</p>
</div>
<div class="service" style="left:770px">
  <div class="service-icon"><div><svg width="38" height="34" viewBox="0 0 38 34"><rect x="2" y="3" width="34" height="22" rx="2" fill="#fff"/><rect x="5" y="6" width="28" height="16" fill="#2f6fba"/><rect x="15" y="25" width="8" height="5" fill="#fff"/><rect x="10" y="29" width="18" height="3" fill="#fff"/></svg></div></div>
  <h3>Diversity and Inclusion<br>management/training</h3>
  <p>It has survived not only five centuries,<br>but also the leap into electronic</p>
</div>

<section class="welcome">
  <div class="welcome-photo" role="img" aria-label="Young colleagues collaborating around a laptop in a bright office"></div>
  <svg class="welcome-panel" width="810" height="455" viewBox="0 0 810 455">
    <defs><linearGradient id="panelGrad" x1="0" y1="0" x2="1" y2="1"><stop offset="0" stop-color="#2a66b2"/><stop offset="1" stop-color="#14468c"/></linearGradient></defs>
    <path d="M0 0 H805 L600 455 H0Z" fill="url(#panelGrad)"/>
    <path d="M0 0 L300 140 L120 455 H0Z" fill="#fff" opacity=".04"/>
    <path d="M300 140 L805 0 L560 280Z" fill="#fff" opacity=".05"/>
  </svg>
  <h2>Welcome To MapleHarbor Partners</h2>
  <p>It is a long established fact that a reader will be distracted by the readable content of a page when looking at its layout. The point of using Lorem Ipsum is that it has a more-or-less normal distribution of letters, as opposed to using 'Content here, content here', making it look like readable English. Many desktop publishing packages and web page editors now use Lorem Ipsum as their default model text, and a search for 'lorem ipsum' will uncover many web sites still in their infancy. Various versions have evolved over the years.</p>
  <div class="btn-outline">Read More »</div>
</section>

<div class="wwd-frame"></div>
<div class="wwd-photo" role="img" aria-label="Smiling businessman in a suit holding a tablet"></div>
<h2 class="heading wwd-title">What We Do</h2>
<p class="wwd-text">It is a long established fact that a reader will be distracted by the readable content of a page when looking at its layout. The point of using Lorem Ipsum is that it has a more-or-less normal distribution of letters, as opposed to using 'Content here, content here',</p>
<ul class="ticks">
  <li><svg width="14" height="12"><path d="M1 6 L5 10 L13 2" fill="none" stroke="#2f6fba" stroke-width="2.4"/></svg>Nullam tempor nisl sit amet risus fermentum, eget consectetur tellus sollicitudin.</li>
  <li><svg width="14" height="12"><path d="M1 6 L5 10 L13 2" fill="none" stroke="#2f6fba" stroke-width="2.4"/></svg>Sed tristique mi ut nunc pulvinar, accumsan congue felis maximus.</li>
  <li><svg width="14" height="12"><path d="M1 6 L5 10 L13 2" fill="none" stroke="#2f6fba" stroke-width="2.4"/></svg>Integer suscipit neque et dui efficitur, id varius diam elementum.</li>
  <li><svg width="14" height="12"><path d="M1 6 L5 10 L13 2" fill="none" stroke="#2f6fba" stroke-width="2.4"/></svg>Sed tristique mi ut nunc pulvinar, accumsan congue felis maximus.</li>
</ul>
<div class="btn-solid">Read More »</div>

<section class="blog">
  <h2 class="heading blog-title">Latest Blog</h2>
  <article class="post" style="left:92px">
    <div class="post-photo" role="img" aria-label="Two colleagues reviewing work at a laptop" style="background:linear-gradient(120deg,#e9eef2,#bcc9d4 60%,#5d7189)"></div>
    <div class="post-meta"><span class="post-date">Dec 03</span><span class="post-comments"><svg width="14" height="11"><path d="M1 1 H13 V8 H6 L3 10 V8 H1Z" fill="none" stroke="#fff" stroke-width="1.3"/></svg></span></div>
    <h4>Neque porro quisquam dolorem</h4>
    <p>It has survived not only five centuries, but also the leap into electronic typesetting,</p>
    <div class="more">Read More »</div>
  </article>
  <article class="post" style="left:438px">
    <div class="post-photo" role="img" aria-label="Man with glasses working at an office desk" style="background:linear-gradient(120deg,#d3d9de,#eef1f3 50%,#9aa6b1)"></div>
    <div class="post-meta"><span class="post-date">Dec 03</span><span class="post-comments"><svg width="14" height="11"><path d="M1 1 H13 V8 H6 L3 10 V8 H1Z" fill="none" stroke="#fff" stroke-width="1.3"/></svg></span></div>
    <h4>Porro quisquam est qui</h4>
    <p>It has survived not only five centuries, but also the leap into electronic typesetting,</p>
    <div class="more">Read More »</div>
  </article>
  <article class="post" style="left:792px">
    <div class="post-photo" role="img" aria-label="Two businessmen discussing in front of a computer" style="background:linear-gradient(120deg,#eef2f5,#c3ced8 55%,#4e6683)"></div>
    <div class="post-meta"><span class="post-date">Dec 03</span><span class="post-comments"><svg width="14" height="11"><path d="M1 1 H13 V8 H6 L3 10 V8 H1Z" fill="none" stroke="#fff" stroke-width="1.3"/></svg></span></div>
    <h4>Dolorem ipsum quia dolor</h4>
    <p>It has survived not only five centuries, but also the leap into electronic typesetting,</p>
    <div class="more">Read More »</div>
  </article>
</section>

<footer class="site-footer">
  <div class="footer-brand"><span class="brand-mark"></span><span class="brand-name">MAPLEHARBOR<br>PARTNERS</span></div>
  <div class="foot-col" style="left:380px">
    <h5>Contact us</h5>
    <p>Address : 720 Harbor Lane Suite 4,<br>FL 33010<br>Phone : 0150 555 0182<br>Email : info@mapleharbor.example</p>
  </div>
  <div class="foot-col" style="left:652px">
    <h5>Join our mailing list</h5>
    <p>Your about us information would fit<br>here nicely.</p>
    <div class="subscribe"><span>Email address</span><span>Submit</span></div>
  </div>
  <div class="foot-col" style="left:946px">
    <h5>Follow us out there</h5>
    <div class="social"><span></span><span></span><span></span><span></span></div>
  </div>
  <div class="foot-rule"></div>
  <div class="copyright">Copyright © 2017. All Rights Reserved</div>
</footer>

</body>
</html>
```